Zielgruppe
Das erzählende Sachbuch 'Allein. Getragen. Heiter. 7 frische Wege zu Fülle und Nähe abseits der Zweisamkeit' richtet sich an Frauen ohne Partner und Kinder.
Im Buch präsentiere ich sieben inspirierende Lebensentwürfe, die zeigen, wie auch ohne Partnerschaft und Familie ein sinnerfülltes Leben in tiefer Verbindung zu anderen möglich ist.
Das Buch lädt alle Frauen (und natürlich auch Männer) ein, anders zu denken und zu leben. Es ermächtigt die Leser:innen, eine liebevolle Perspektive auf ihr Sololeben einzunehmen und ihren eigenen, außergewöhnlichen Weg zu gehen, kurzum: glücklich-verbunden zu leben.
Die Zielgruppe sind moderne Frauen jeden Alters, die offen für das Thema Persönlichkeitsentwicklung sind und ihr Glück selbst in die Hand nehmen.
Aufgabenstellung
Text Cover:
Buchtitel: Allein. Getragen. Heiter.
Untertitel: 7 frische Wege zu Fülle und Nähe abseits der Zweisamkeit
Störer: Mit inspirierenden Tipps zur Umsetzung
Autorin: Jule Henrike Brandt
Format:
Das Buch wird als Taschenbuch bei WLV veröffentlicht, im Format 13,34 x 20,32 cm (5,25 x 8 Zoll). Die Vorlage für das Layout des Buchcovers (Titelseite, Seitenleiste, Rückseite) ist hier angehängt. Es wird benötigt: Titelseite, Seitenleiste, Rückseite mit Klappentext und Platzhalter für Barcode. Bitte beachten: Das Buch wird gerade gesetzt. Eventuell muss die Breite des Buchrückens am Ende noch angepasst werden, je nach finaler Seitenzahl.
Inhalt:
Das Cover soll eine Frau zeigen, da im Titel nicht explizit von Frauen gesprochen wird, die Zielgruppe des Buches aber Frauen sind. Diese soll eher schematisch dargestellt sein, damit möglichst viele Frauen sich mit ihr identifizieren können. Sie soll glücklich wirken. Falls Details zu sehen sind: mitteleuropäisch, Haarfarbe hellbraun, Augenfarbe blau oder grün. Wenn möglich, sollte ihre 'Verbindung' (z.B. zu anderen, zum Universum, zur Natur) dargestellt werden, ohne dass es sehr esoterisch wirkt.
Der Titel des Buches sollte groß genug sein, um auch als kleines Thumbnail in der Bücherfloß-Suche oder bei den Empfehlungen gelesen werden zu können. Der Name der Autorin kann klein sein. Gerne kann ein Emblem oder kleines Logo eingefügt werden, an der Stelle, an der ansonsten der Verlag steht (gerne die Sonne, die auch im Inneren des Buches als Verzierung verwendet wird – Icon hier angehängt).
Stil:
Ich lade hier eine Idee hoch, die ganz grob in die richtige Richtung geht. Die Farben (Helllila und Anthrazit) in der Kombination gefallen mir, da es weiblich, aber nicht zu süß aussieht. Die Frau sieht aber in diesem Layout nicht glücklich aus, das sollte geändert werden. Das Layout soll modern und clean, aber nicht nüchtern aussehen.

```html
<!DOCTYPE html>
<html lang="de">
<head>
<meta charset="utf-8">
<title>Allein. Getragen. Heiter. – Buchumschlag</title>
<link rel="stylesheet" href="https://fonts.googleapis.com/css2?family=Archivo:wdth,wght@125,800&family=Manrope:wght@300;400;500&display=swap">
<style>
  :root {
    --backdrop: #455f86;
    --cover-top: #7f97d0;
    --cover-bottom: #7a93cc;
    --back-bottom: #5b79c6;
    --spine: #6580cc;
    --ink-light: #ffffff;
    --stoerer: #e8982a;
    --stoerer-text: #fff5e6;
    --art-a: #8fa0d6;
    --art-b: #b9a0c9;
  }
  * { box-sizing: border-box; margin: 0; padding: 0; }
  html, body { width: 1200px; height: 960px; overflow: hidden; }
  body {
    background: var(--backdrop);
    font-family: "Manrope", sans-serif;
    color: var(--ink-light);
    position: relative;
  }
  .wrap {
    position: absolute;
    left: 80px; top: 100px;
    width: 1040px; height: 760px;
    display: flex;
    box-shadow: 0 18px 40px rgba(20, 30, 55, .35);
  }

  /* Rückseite */
  .back-cover {
    width: 500px; height: 100%;
    background: linear-gradient(180deg, var(--cover-top) 0%, var(--cover-bottom) 55%, var(--back-bottom) 100%);
    padding: 52px 46px 0 52px;
  }
  .back-title {
    font-family: "Archivo", sans-serif;
    font-weight: 800;
    font-stretch: 125%;
    font-size: 22px;
    letter-spacing: .5px;
    margin-bottom: 40px;
  }
  .blurb p {
    font-size: 13.2px;
    line-height: 1.5;
    font-weight: 400;
    margin-bottom: 18px;
  }

  /* Buchrücken */
  .spine {
    width: 40px; height: 100%;
    background: var(--spine);
    position: relative;
    border-left: 1px solid rgba(255,255,255,.12);
    border-right: 1px solid rgba(40,60,120,.18);
  }
  .spine-emblem {
    position: absolute; left: 10px; top: 26px;
    width: 20px; height: 20px; border-radius: 50%;
    background: rgba(255,255,255,.35);
  }
  .spine-text {
    position: absolute; left: 50%; top: 80px;
    writing-mode: vertical-rl;
    transform: translateX(-50%);
    white-space: nowrap;
  }
  .spine-author { font-size: 9.5px; letter-spacing: 1px; font-weight: 400; }
  .spine-title {
    font-family: "Archivo", sans-serif; font-weight: 800; font-stretch: 125%;
    font-size: 10px; letter-spacing: .6px; margin-top: 70px;
  }

  /* Titelseite */
  .front-cover {
    width: 500px; height: 100%;
    background: linear-gradient(180deg, var(--cover-top), var(--cover-bottom));
    position: relative;
    overflow: hidden;
  }
  .cover-art {
    position: absolute; left: 40px; top: 0;
    width: 440px; height: 420px;
    background: linear-gradient(160deg, var(--art-a) 0%, var(--art-b) 60%, var(--art-a) 100%);
    opacity: .75;
  }
  .author {
    position: absolute; top: 48px; left: 0; right: 0;
    text-align: center;
    font-size: 14px; font-weight: 400; letter-spacing: .6px;
  }
  .stoerer {
    position: absolute; left: 306px; top: 370px;
    width: 118px; height: 118px; border-radius: 50%;
    background: var(--stoerer);
    color: var(--stoerer-text);
    display: flex; align-items: center; justify-content: center;
    text-align: center;
    font-size: 13px; line-height: 1.18; font-weight: 400;
    padding: 0 10px;
  }
  .title {
    position: absolute; left: 54px; top: 470px;
    font-family: "Archivo", sans-serif; font-weight: 800; font-stretch: 125%;
    font-size: 44px; line-height: 1.08; letter-spacing: .5px;
  }
  .subtitle {
    position: absolute; left: 54px; top: 634px;
    display: flex; align-items: center; gap: 18px;
  }
  .subtitle-num {
    font-family: "Archivo", sans-serif; font-weight: 800; font-size: 34px;
  }
  .subtitle-text { font-size: 14px; line-height: 1.3; font-weight: 400; letter-spacing: .3px; }
  .emblem {
    position: absolute; left: 232px; top: 700px;
    width: 36px; height: 36px; border-radius: 50%;
    background: rgba(255,255,255,.3);
  }
</style>
</head>
<body>
  <div class="wrap">
    <section class="back-cover">
      <h2 class="back-title">ALLEIN.</h2>
      <div class="blurb">
        <p>Single- und kinderlose Frauen zählen Studien zufolge zu den glücklichsten Menschen. Doch die Gesellschaft sieht sie oft als bemitleidenswerte Außenseiterinnen. Viele Singles übernehmen diesen Blick auf sich selbst, fühlen sich unvollständig oder als Versagerinnen.</p>
        <p>Die Sozialanthropologin Jule Henrike Brandt findet: Das Ideal der Mutter und Partnerin ist unangefochten, während es kaum alternative, positive Ideale für Frauen gibt. Also hat sie sich auf die Suche nach Alternativen gemacht – und sie gefunden: in anderen Teilen der Welt, in Kultur und Literatur, in der Geschichte und, nicht zuletzt, in ihrem eigenen Leben. Hier präsentiert sie sieben inspirierende Lebensentwürfe, die zeigen, wie auch ohne Partnerschaft und Familie ein sinnerfülltes Leben in tiefer Verbindung zu anderen möglich ist. Sie teilt natürlich ihre eigenen Erfahrungen – etwa als „Hüterin der Freundschaft“ oder „Dienerin des Lebens“ – und verbindet sie mit inspirierenden Ansätzen aus der Persönlichkeitsentwicklung.</p>
        <p>Das Buch lädt alle Frauen und natürlich auch Männer ein, anders zu denken und zu leben. Es ermächtigt die Leser:innen, eine liebevolle Perspektive auf ihr Sololeben einzunehmen und ihren eigenen, außergewöhnlichen Weg zu gehen, kurzum:</p>
        <p>glücklich-verbunden zu leben.</p>
      </div>
    </section>

    <aside class="spine">
      <div class="spine-emblem" role="img" aria-label="Kleines Sonnen-Emblem"></div>
      <div class="spine-text">
        <span class="spine-author">JULE HENRIKE BRANDT</span>
        <span class="spine-title">ALLEIN. GETRAGEN. HEITER.</span>
      </div>
    </aside>

    <section class="front-cover">
      <div class="cover-art" role="img" aria-label="Illustration: eine Frau schwebt gelöst im Blau und hält die Hände zweier Menschen, die von oben und von der Seite nach ihr greifen"></div>
      <p class="author">JULE HENRIKE BRANDT</p>
      <div class="stoerer">Mit inspirierenden Tipps zur Umsetzung</div>
      <h1 class="title">ALLEIN.<br>GETRAGEN.<br>HEITER.</h1>
      <div class="subtitle">
        <span class="subtitle-num">7</span>
        <span class="subtitle-text">frische Wege zu Fülle und Nähe<br>abseits der Zweisamkeit</span>
      </div>
      <div class="emblem" role="img" aria-label="Sonnen-Emblem"></div>
    </section>
  </div>
</body>
</html>
```